Waffle packs (for hard discounters)

Waffle packs – Hard discounter – Design Brief - front panel only
We need a pack designed for our Brussels style waffles. The packs are retail packs for sale and distribution in supermarkets (hard discounters). The requirement is for a complete design for the front panel (5 varieties). The design could include a logo for the brand "Mira Poldt" or the look and stylised text could be the 'logo".
Brand name: MIRA POLDT, Mira Poldt, mira poldt
General:
• 8 Waffles in a clear foil pack (see attached)
• Most of the front view should be clear (show case the product)
• Design should work for all varieties from the dark chocolate, chocolate coated waffles to lighter fresh (plain) waffles
• Should look delicious/edible, but have some of the look and feel of a hard discounter (Vemo, Koru,..) label. Hard discount can have the kook of luxury/quality, not just cheap and cheerful. (see sample label/pack attached of hard discounter own brand)
• Could be ~3 or 4 colours spot. Gold could be a possible colour
• Colours will include white (white will be minimum foundation behind all print) and black (or dark brown)
• Ideally change of variety will be changed in one colour only (most likely the black). All other colours being come to the design of all varieties
• Dielines (see attached) front panel 140mm (w) x 180 mm (h)
Varieties:
5 – “Brussels Style Waffles”
• Fresh Egg Waffles or Brussels Style Fresh Egg Waffles
• Cinnamon Waffles or ……
• Chocolate Waffles or ……
• Choc Topped Waffles or ……
• Lamington Waffles or ……
Other text on front panel:
• No Artificial Colours
• No Preservatives
• Made with Fresh Eggs
• 165g
• 8 waffles or 8 WAFFLES or 8 Waffles
• Optional creative text: e.g. Perfect any time of day….breakfast, snacks, dessert….
Barcode on the front (see spec. attached):
Updates
Note: on the pack. The seams/join run down the sides (left and right), not top and bottom as shown in one of my pictures.
Industry/Entity Type
Food Production
Requirements
Should not have
- The waffle packs in Photos (19),zip are just to show the real product in a pack. With real product and showing the joins/seams are on the sides. These packs are not the design brief.

```html
<!DOCTYPE html>
<html lang="en">
<head>
<meta charset="utf-8">
<title>Mira Poldt Waffle Packs</title>
<link rel="stylesheet" href="https://fonts.googleapis.com/css2?family=Chewy&family=Mrs+Saint+Delafield&family=Zilla+Slab:wght@500;600&display=swap">
<style>
  :root{
    --board:#ffffff;
    --stage:#ececec;
    --black:#000000;
    --yellow:#fdd000;
    --choc:#6b3219;
    --cinnamon:#f2a261;
    --maroon:#5e2a2c;
    --choco-top:#6d2e2b;
    --lamington:#d5b8a6;
    --white:#ffffff;
    --cream:#fbf6e6;
    --pink:#df7b8e;
    --ink:#1b1b1b;
    --bite-light:#d9a872;
    --bite-mid:#a8653a;
    --bite-dark:#4a2414;
  }
  *{margin:0;padding:0;box-sizing:border-box}
  html,body{width:1200px;height:1035px;overflow:hidden;background:var(--board)}
  .board{position:relative;width:1200px;height:1035px}
  .stage{position:absolute;background:var(--stage)}
  .stage--top{left:800px;top:30px;width:400px;height:468px}
  .stage--bottom{left:798px;top:532px;width:402px;height:468px}

  .pack{position:absolute;overflow:hidden;font-size:10px;background:var(--lower)}
  .pack--small{font-size:8.4px}
  .pack__art{position:absolute;inset:0;width:100%;height:100%}
  .pack__photo{position:absolute;left:0;right:0;bottom:0;height:25%;
    background:linear-gradient(180deg,var(--bite-light) 0%,var(--bite-mid) 55%,var(--bite-dark) 100%);
    clip-path:polygon(0 32%,27% 9%,37% 0,68% 0,78% 9%,100% 36%,100% 100%,0 100%)}
  .pack__title{position:absolute;left:0;right:0;top:8%;text-align:center;white-space:nowrap;
    font-family:'Chewy',cursive;font-weight:400;font-size:3.4em;line-height:1;color:var(--title);
    transform:rotate(7deg);text-shadow:0.04em 0.06em 0 var(--title-shadow)}
  .pack__tagline{position:absolute;left:50%;top:29%;white-space:nowrap;
    font-family:'Mrs Saint Delafield',cursive;font-size:2.7em;line-height:1;color:var(--white);
    transform:translate(-50%,-50%) rotate(-24deg)}
  .pack__seal{position:absolute;left:50%;top:47%;width:37%;aspect-ratio:1;
    transform:translate(-50%,-50%);border-radius:50%;background:var(--cream);
    border:0.8em solid var(--pink);display:flex;align-items:center;justify-content:center;text-align:center}
  .pack__brand{font-family:'Zilla Slab',serif;font-weight:600;font-size:2.8em;line-height:0.95;color:var(--pink)}
  .pack__claims{position:absolute;left:0;right:0;top:63%;text-align:center;list-style:none;
    font-family:'Zilla Slab',serif;font-weight:500;font-size:1.45em;line-height:1.5;color:var(--claims)}

  .pack--fresh-egg{left:12px;top:8px;width:388px;height:498px;
    --upper:var(--black);--lower:var(--yellow);--title:var(--yellow);--title-shadow:#6b4e00;--claims:var(--ink);--arrow:var(--ink)}
  .pack--chocolate{left:409px;top:8px;width:388px;height:498px;
    --upper:var(--black);--lower:var(--choc);--title:#e9a96a;--title-shadow:#5a3418;--claims:var(--white);--arrow:var(--white)}
  .pack--cinnamon{left:836px;top:64px;width:328px;height:404px;
    --upper:#1a1a1a;--lower:var(--cinnamon);--title:#e9a06a;--title-shadow:#5a3418;--claims:#4a2e1c;--arrow:var(--ink)}
  .pack--choco-top{left:10px;top:516px;width:388px;height:500px;
    --upper:var(--maroon);--lower:var(--white);--title:var(--white);--title-shadow:#1b1b1b;--claims:var(--ink);--arrow:var(--ink)}
  .pack--lamington{left:406px;top:516px;width:388px;height:500px;
    --upper:var(--lamington);--lower:var(--white);--title:var(--white);--title-shadow:#5e2a2c;--claims:var(--ink);--arrow:var(--ink)}
  .pack--choco-top-alt{left:840px;top:568px;width:320px;height:400px;
    --upper:var(--choco-top);--lower:var(--white);--title:var(--white);--title-shadow:#1b1b1b;--claims:var(--ink);--arrow:var(--ink)}

  .band{fill:var(--upper)}
  .arrow{fill:none;stroke:var(--arrow);stroke-width:4;stroke-linecap:round;stroke-linejoin:round}
</style>
</head>
<body>
<div class="board">
  <div class="stage stage--top"></div>
  <div class="stage stage--bottom"></div>

  <section class="pack pack--fresh-egg">
    <svg class="pack__art" viewBox="0 0 485 623" preserveAspectRatio="none" aria-hidden="true">
      <polygon class="band" points="0,0 485,0 485,262 242,330 0,268"/>
      <path class="arrow" d="M148 418 C120 392 78 398 66 428 C58 450 82 456 80 440 C77 424 56 438 52 462 M42 450 L52 464 L62 452"/>
      <path class="arrow" d="M337 418 C365 392 407 398 419 428 C427 450 403 456 405 440 C408 424 429 438 433 462 M443 450 L433 464 L423 452"/>
    </svg>
    <div class="pack__photo" role="img" aria-label="Photo of Brussels waffles with chocolate drizzle, raspberries and icing sugar"></div>
    <h2 class="pack__title">Fresh Egg Waffles</h2>
    <p class="pack__tagline">The twist you can't resist!</p>
    <div class="pack__seal"><span class="pack__brand">Mira<br>Poldt</span></div>
    <ul class="pack__claims"><li>No Artificial Colours</li><li>No Preservatives</li><li>Made with Fresh Eggs</li><li>8 Waffles • 165 g</li></ul>
  </section>

  <section class="pack pack--chocolate">
    <svg class="pack__art" viewBox="0 0 485 623" preserveAspectRatio="none" aria-hidden="true">
      <polygon class="band" points="0,0 485,0 485,262 242,330 0,268"/>
      <path class="arrow" d="M148 418 C120 392 78 398 66 428 C58 450 82 456 80 440 C77 424 56 438 52 462 M42 450 L52 464 L62 452"/>
      <path class="arrow" d="M337 418 C365 392 407 398 419 428 C427 450 403 456 405 440 C408 424 429 438 433 462 M443 450 L433 464 L423 452"/>
    </svg>
    <div class="pack__photo" role="img" aria-label="Photo of Brussels waffles with chocolate drizzle, raspberries and icing sugar"></div>
    <h2 class="pack__title">Chocolate Waffles</h2>
    <p class="pack__tagline">The twist you can't resist!</p>
    <div class="pack__seal"><span class="pack__brand">Mira<br>Poldt</span></div>
    <ul class="pack__claims"><li>No Artificial Colours</li><li>No Preservatives</li><li>Made with Fresh Eggs</li><li>8 Waffles • 165 g</li></ul>
  </section>

  <section class="pack pack--cinnamon pack--small">
    <svg class="pack__art" viewBox="0 0 485 623" preserveAspectRatio="none" aria-hidden="true">
      <polygon class="band" points="0,0 485,0 485,300 242,330 0,300"/>
      <path class="arrow" d="M148 418 C120 392 78 398 66 428 C58 450 82 456 80 440 C77 424 56 438 52 462 M42 450 L52 464 L62 452"/>
      <path class="arrow" d="M337 418 C365 392 407 398 419 428 C427 450 403 456 405 440 C408 424 429 438 433 462 M443 450 L433 464 L423 452"/>
    </svg>
    <div class="pack__photo" role="img" aria-label="Photo of Brussels waffles with chocolate drizzle, raspberries and icing sugar"></div>
    <h2 class="pack__title">Cinnamon Waffles</h2>
    <p class="pack__tagline">The twist you can't resist!</p>
    <div class="pack__seal"><span class="pack__brand">Mira<br>Poldt</span></div>
    <ul class="pack__claims"><li>No Artificial Colours</li><li>No Preservatives</li><li>Made with Fresh Eggs</li><li>8 Waffles • 165 g</li></ul>
  </section>

  <section class="pack pack--choco-top">
    <svg class="pack__art" viewBox="0 0 485 623" preserveAspectRatio="none" aria-hidden="true">
      <polygon class="band" points="0,0 485,0 485,262 242,330 0,262"/>
      <path class="arrow" d="M148 418 C120 392 78 398 66 428 C58 450 82 456 80 440 C77 424 56 438 52 462 M42 450 L52 464 L62 452"/>
      <path class="arrow" d="M337 418 C365 392 407 398 419 428 C427 450 403 456 405 440 C408 424 429 438 433 462 M443 450 L433 464 L423 452"/>
    </svg>
    <div class="pack__photo" role="img" aria-label="Photo of Brussels waffles with chocolate drizzle, raspberries and icing sugar"></div>
    <h2 class="pack__title">Choco Top Waffles</h2>
    <p class="pack__tagline">The twist you can't resist!</p>
    <div class="pack__seal"><span class="pack__brand">Mira<br>Poldt</span></div>
    <ul class="pack__claims"><li>No Artificial Colours</li><li>No Preservatives</li><li>Made with Fresh Eggs</li><li>8 Waffles • 165 g</li></ul>
  </section>

  <section class="pack pack--lamington">
    <svg class="pack__art" viewBox="0 0 485 623" preserveAspectRatio="none" aria-hidden="true">
      <polygon class="band" points="0,0 485,0 485,262 242,330 0,262"/>
      <path class="arrow" d="M148 418 C120 392 78 398 66 428 C58 450 82 456 80 440 C77 424 56 438 52 462 M42 450 L52 464 L62 452"/>
      <path class="arrow" d="M337 418 C365 392 407 398 419 428 C427 450 403 456 405 440 C408 424 429 438 433 462 M443 450 L433 464 L423 452"/>
    </svg>
    <div class="pack__photo" role="img" aria-label="Photo of Brussels waffles with chocolate drizzle, raspberries and icing sugar"></div>
    <h2 class="pack__title">Lamington Waffles</h2>
    <p class="pack__tagline">The twist you can't resist!</p>
    <div class="pack__seal"><span class="pack__brand">Mira<br>Poldt</span></div>
    <ul class="pack__claims"><li>No Artificial Colours</li><li>No Preservatives</li><li>Made with Fresh Eggs</li><li>8 Waffles • 165 g</li></ul>
  </section>

  <section class="pack pack--choco-top-alt pack--small">
    <svg class="pack__art" viewBox="0 0 485 623" preserveAspectRatio="none" aria-hidden="true">
      <polygon class="band" points="0,0 485,0 485,300 242,330 0,300"/>
      <path class="arrow" d="M148 418 C120 392 78 398 66 428 C58 450 82 456 80 440 C77 424 56 438 52 462 M42 450 L52 464 L62 452"/>
      <path class="arrow" d="M337 418 C365 392 407 398 419 428 C427 450 403 456 405 440 C408 424 429 438 433 462 M443 450 L433 464 L423 452"/>
    </svg>
    <div class="pack__photo" role="img" aria-label="Photo of Brussels waffles with chocolate drizzle, raspberries and icing sugar"></div>
    <h2 class="pack__title">Choco Top Waffles</h2>
    <p class="pack__tagline">The twist you can't resist!</p>
    <div class="pack__seal"><span class="pack__brand">Mira<br>Poldt</span></div>
    <ul class="pack__claims"><li>No Artificial Colours</li><li>No Preservatives</li><li>Made with Fresh Eggs</li><li>8 Waffles • 165 g</li></ul>
  </section>
</div>
</body>
</html>
```